Cover of the e-book award-winning national sports figure.

I would like to utilize the picture this attached to this brief. If you could pull the trophies and myself out and place with the new background, that’s what I would like to see . I would like to have a new bookcover design for my e-book. I attached below the original cover and have marked in red. The things that I don’t want on the new cover. I’ve attached a picture that’s not the original. I’m waiting on the high copy. I would like to replace the old logo with the one that I have attached. The website that I would like to have on the book is www.dellanvmoreaux.com.
Target Market(s)
Biography
Industry/Entity Type
Sports & motivation?
Requirements
Must have
- Picture of me in the blue suit on the cover the title of the book walking past midnight lessons from quiet harbors
Nice to have
- Utilize the old cover that I have attached for some ideas
Should not have
- The cover should not have anything related to marlow crest press Inc.

```html
<!DOCTYPE html>
<html lang="en">
<head>
<meta charset="utf-8">
<title>Walking Past Midnight — Book Cover</title>
<link rel="stylesheet" href="https://fonts.googleapis.com/css2?family=Inter:wght@600;700&family=Source+Serif+4:ital,wght@0,700;1,600&display=swap">
<style>
  :root {
    --stage: #cfdbf5;
    --navy: #283562;
    --mist: #d3ddf5;
    --gold-light: #f3e4c4;
    --gold: #c9b08a;
    --gold-dark: #8c7355;
    --subtitle: #efe0c0;
    --photo-a: #3d5a9e;
    --photo-b: #1f2f5c;
    --trophy-a: #e6e8ee;
    --trophy-b: #8d9099;
  }
  html, body {
    margin: 0;
    width: 1200px;
    height: 1200px;
    overflow: hidden;
    background: var(--stage);
  }
  .book-cover {
    position: absolute;
    left: 240px;
    top: 60px;
    width: 720px;
    height: 1080px;
    background: var(--navy);
    overflow: hidden;
  }
  .cover-art {
    position: absolute;
    inset: 0;
  }
  .title-line {
    font-family: "Inter", Arial, sans-serif;
    font-weight: 700;
  }
  .subtitle {
    position: absolute;
    left: 400px;
    top: 258px;
    margin: 0;
    font-family: "Inter", Arial, sans-serif;
    font-weight: 600;
    font-size: 42px;
    line-height: 1.12;
    color: var(--subtitle);
  }
  .author {
    position: absolute;
    left: 40px;
    top: 660px;
    margin: 0;
    font-family: "Source Serif 4", Georgia, serif;
    font-weight: 700;
    font-size: 60px;
    line-height: 1.08;
    letter-spacing: 1px;
    color: var(--navy);
  }
  .foreword {
    position: absolute;
    left: 40px;
    top: 838px;
    margin: 0;
    font-family: "Source Serif 4", Georgia, serif;
    font-style: italic;
    font-weight: 600;
    font-size: 38px;
    line-height: 1.25;
    color: var(--navy);
  }
  .author-photo {
    position: absolute;
    left: 450px;
    top: 640px;
    width: 270px;
    height: 440px;
    background: linear-gradient(180deg, var(--photo-a), var(--photo-b));
  }
  .trophy-photo {
    position: absolute;
    left: 335px;
    top: 870px;
    width: 115px;
    height: 210px;
    background: linear-gradient(180deg, var(--trophy-a), var(--trophy-b));
  }
</style>
</head>
<body>
  <main class="book-cover">
    <svg class="cover-art" width="720" height="1080" viewBox="0 0 720 1080">
      <defs>
        <linearGradient id="goldFill" x1="0" y1="0" x2="0" y2="1">
          <stop offset="0" stop-color="var(--gold-light)"/>
          <stop offset="0.5" stop-color="var(--gold)"/>
          <stop offset="1" stop-color="var(--gold-light)"/>
        </linearGradient>
        <linearGradient id="bandFill" x1="0" y1="0" x2="1" y2="0">
          <stop offset="0" stop-color="var(--gold-dark)"/>
          <stop offset="0.6" stop-color="var(--gold-light)"/>
          <stop offset="1" stop-color="var(--gold)"/>
        </linearGradient>
      </defs>
      <path class="lower-panel-band" d="M0,572 C260,548 520,640 720,860 L720,1080 L0,1080 Z" fill="url(#bandFill)"/>
      <path class="lower-panel" d="M0,586 C255,566 510,655 720,884 L720,1080 L0,1080 Z" fill="var(--mist)"/>
      <g class="title" fill="url(#goldFill)" stroke="var(--gold-dark)" stroke-width="2">
        <text class="title-line" x="38" y="215" font-size="190" textLength="644" lengthAdjust="spacingAndGlyphs">WALKING</text>
        <text class="title-line" x="38" y="372" font-size="160" textLength="340" lengthAdjust="spacingAndGlyphs">PAST</text>
        <text class="title-line" x="38" y="528" font-size="160" textLength="644" lengthAdjust="spacingAndGlyphs">MIDNIGHT</text>
      </g>
    </svg>
    <p class="subtitle">Lessons from<br>Quiet Harbors</p>
    <p class="author">DELLAN V.<br>MOREAUX</p>
    <p class="foreword">Foreword by<br>Marcus Ellery</p>
    <div class="trophy-photo" role="img" aria-label="Photo of two silver championship trophies"></div>
    <div class="author-photo" role="img" aria-label="Photo of the author standing in a blue pinstripe suit"></div>
  </main>
</body>
</html>
```